Design a flyer promoting a baseball tournament, similar to what is attached.
Date: September 16-17th
Location: Denver, CO
Prize: $5k minimum
Name: Harlan Voss Classic
Misc:
* Memorial Scholarship giveaway
* Invite Only
* Sponsored By Mesa Falcons
* No entry fee

Target Market(s)

Baseball Teams, Adult

Industry/Entity Type

Recreation

Colors
0455a3
eaf1f7
85cae6

Requirements
Must have
• Tournament Details and info
Nice to have
• dynamic graphics supporting the Denver area landscape

```html
<!DOCTYPE html>
<html lang="en">
<head>
<meta charset="utf-8">
<title>Harlan Voss Classic – Tournament Flyer</title>
<link rel="stylesheet" href="https://fonts.googleapis.com/css2?family=Graduate&family=Tinos&family=Zilla+Slab:wght@700&display=swap">
<style>
  :root {
    --brand-blue: #0455a3;
    --ice: #eaf1f7;
    --sky: #85cae6;
    --navy: #0b1f4d;
    --ink: #111111;
    --stage: #4a4a4a;
    --paper: #ffffff;
  }
  * { margin: 0; padding: 0; box-sizing: border-box; }
  html, body {
    width: 1200px; height: 1200px; overflow: hidden;
    background: var(--stage);
  }
  .flyer {
    position: absolute; left: 210px; top: 95px;
    width: 780px; height: 1011px;
    background: var(--paper);
  }
  .sponsor-label {
    position: absolute; top: 30px; left: 0; width: 100%;
    text-align: center;
    font: 28px "Tinos", serif;
    letter-spacing: 0.5em; padding-left: 0.5em;
    color: var(--ink);
  }
  .hero-art {
    position: absolute; left: 34px; top: 116px;
    width: 710px; height: 659px; border-radius: 12px;
    background: linear-gradient(180deg, #0b1a45 0%, #1a3a86 32%, #2b56a8 55%, #355f78 70%, #3f8a3e 82%, #2f6b2f 100%);
  }
  .sponsor-name {
    position: absolute; top: 120px; left: 0; width: 100%;
    text-align: center;
    font: 700 54px "Zilla Slab", serif;
    color: var(--sky);
  }
  .headline {
    position: absolute; left: 0; top: 0; width: 780px; height: 780px;
    overflow: visible;
    filter: drop-shadow(5px 7px 0 var(--navy));
  }
  .headline text {
    font-family: "Graduate", serif;
    fill: url(#headline-fill);
    stroke: var(--brand-blue); stroke-width: 12px;
    stroke-linejoin: round; paint-order: stroke;
  }
  .event-name {
    position: absolute; left: 34px; top: 788px; width: 716px;
    font: 50px "Graduate", serif; color: var(--brand-blue);
    text-align: center; letter-spacing: 0.02em; white-space: nowrap;
    -webkit-text-stroke: 1.5px var(--brand-blue);
  }
  .details {
    position: absolute; left: 46px; top: 852px; list-style: none;
  }
  .details li {
    display: flex; align-items: center; height: 44px;
    font: 35px "Tinos", serif; color: var(--ink);
  }
  .details svg { width: 34px; height: 34px; margin-right: 14px; fill: var(--brand-blue); }
  .divider {
    position: absolute; left: 476px; top: 858px; width: 2px; height: 132px;
    background: linear-gradient(180deg, #bbb, #888);
  }
  .perks { position: absolute; left: 510px; top: 855px; list-style: none; width: 260px; }
  .perks li {
    position: relative; padding-left: 20px; margin-bottom: 9px;
    font: 700 14.5px/18px "Zilla Slab", serif; color: var(--ink);
  }
  .perks svg { position: absolute; left: -2px; top: 1px; width: 18px; height: 18px; }
</style>
</head>
<body>
<main class="flyer">
  <p class="sponsor-label">SPONSORED BY</p>

  <div class="hero-art" role="img" aria-label="Night city skyline above a floodlit baseball stadium with crossed wooden bats, a large baseball and a leather glove"></div>

  <p class="sponsor-name">Mesa Falcons</p>

  <svg class="headline" viewBox="0 0 780 780" aria-label="World Series of Baseball">
    <defs>
      <linearGradient id="headline-fill" x1="0" y1="0" x2="0" y2="1">
        <stop offset="0" stop-color="#ffffff"/>
        <stop offset="0.55" stop-color="#f4f6f9"/>
        <stop offset="1" stop-color="#9aa7b6"/>
      </linearGradient>
    </defs>
    <g transform="rotate(-2 390 540)">
      <text x="110" y="482" font-size="172" textLength="544" lengthAdjust="spacingAndGlyphs">WORLD</text>
      <text x="126" y="600" font-size="140" textLength="544" lengthAdjust="spacingAndGlyphs">SERIES OF</text>
      <text x="134" y="716" font-size="140" textLength="552" lengthAdjust="spacingAndGlyphs">BASEBALL</text>
    </g>
  </svg>

  <h1 class="event-name">HARLAN VOSS CLASSIC</h1>

  <ul class="details">
    <li>
      <svg viewBox="0 0 24 24" aria-hidden="true"><path d="M6 1h2v3H6zM16 1h2v3h-2zM2 4h20v19H2zm2 5v12h16V9zm1 1h3v3H5zm4 0h3v3H9zm4 0h3v3h-3zm4 0h2v3h-2zM5 14h3v3H5zm4 0h3v3H9zm4 0h3v3h-3zm4 0h2v3h-2zM5 18h3v2H5zm4 0h3v2H9zm4 0h3v2h-3z"/></svg>
      SEPTEMBER 16-17TH
    </li>
    <li>
      <svg viewBox="0 0 24 24" aria-hidden="true"><path d="M12 1a8 8 0 0 0-8 8c0 6 8 14 8 14s8-8 8-14a8 8 0 0 0-8-8zm0 11a3.3 3.3 0 1 1 0-6.6 3.3 3.3 0 0 1 0 6.6z"/></svg>
      DENVER, CO
    </li>
    <li>
      <svg viewBox="0 0 24 24" aria-hidden="true"><path d="M6 2h12v2h4v3a5 5 0 0 1-5 5 6 6 0 0 1-4 3v3h4v4H7v-4h4v-3a6 6 0 0 1-4-3 5 5 0 0 1-5-5V4h4zm0 4H4v1a3 3 0 0 0 2 3zm12 0v4a3 3 0 0 0 2-3V6z"/></svg>
      $5K MINIMUM
    </li>
  </ul>

  <div class="divider"></div>

  <ul class="perks">
    <li><svg viewBox="0 0 20 20" aria-hidden="true"><path d="M2 11l5 6L18 3" fill="none" stroke="#0455a3" stroke-width="3"/></svg>MEMORIAL SCHOLARSHIP GIVEAWAY</li>
    <li><svg viewBox="0 0 20 20" aria-hidden="true"><path d="M2 11l5 6L18 3" fill="none" stroke="#0455a3" stroke-width="3"/></svg>INVITE ONLY</li>
    <li><svg viewBox="0 0 20 20" aria-hidden="true"><path d="M2 11l5 6L18 3" fill="none" stroke="#0455a3" stroke-width="3"/></svg>SPONSORED BY MESA FALCONS</li>
    <li><svg viewBox="0 0 20 20" aria-hidden="true"><path d="M2 11l5 6L18 3" fill="none" stroke="#0455a3" stroke-width="3"/></svg>NO ENTRY FEE</li>
  </ul>
</main>
</body>
</html>
```